Ecommerce site that acts also as a portal for B2C members and non- members and B2B. Please see attachment this is for only front end work, backend will follow. Husk and Kettle- a MRWE Hospitality Company

Products
Coffee bean sourcing, acquisition, roasting, grinding, blending, sale/delivery
Tea sourcing, acquisition, roasting, grinding, blending, sale/delivery
Applicable/Associated Merchandise and Accoutrements

Initial market penetration for both B2C and B2B offering Husk and Kettle custom blends of both Coffees and Teas.
B2C- Brindle style sale/distribution via guest and members. Members initial fee $129 annual $99 a year thereafter with benefits such as 1st year gift of a French Press Travel Mug (customized/logo/name/brand), monthly samples. Attached document has non project related information for narrative and conceptual inputs.

```html
<!DOCTYPE html>
<html lang="en">
<head>
<meta charset="utf-8">
<title>Husk and Kettle — Artisan Coffee and Tea</title>
<link rel="stylesheet" href="https://fonts.googleapis.com/css2?family=Marcellus&family=Poppins:ital,wght@0,300;0,400;0,500;0,600;1,400&display=swap">
<style>
:root{
  --accent:#b5803f;
  --brown:#4a2b1d;
  --dark:#2b1a10;
  --ink:#2a1a12;
  --muted:#5b4a40;
  --light:#e9e8ea;
  --paper:#ffffff;
}
*{box-sizing:border-box;margin:0;padding:0}
html,body{width:1200px;height:5164px;overflow:hidden}
body{font-family:"Poppins",sans-serif;color:var(--ink);background:var(--paper);position:relative}
.serif{font-family:"Marcellus",serif;font-weight:400}
section,header,footer{position:absolute;left:0;width:1200px;overflow:hidden}
.abs{position:absolute}
.btn{position:absolute;display:flex;align-items:center;justify-content:center;background:var(--accent);color:#fff;font-size:10px;font-weight:600;border-radius:0 10px 0 10px;height:36px}
.ph{position:absolute}
p{font-size:10px;line-height:17px}

/* header */
.site-header{top:0;height:70px;background:#fff}
.brand{left:118px;top:22px;display:flex;align-items:center;gap:8px;font-family:"Marcellus",serif;font-size:15px;color:var(--ink)}
.brand i{display:block;width:22px;height:22px;border-radius:50%;background:var(--accent)}
.nav{left:416px;top:28px;display:flex;gap:18px;font-size:10px}
.nav .on{color:var(--accent)}
.tools{left:976px;top:27px;display:flex;gap:28px}

/* hero */
.hero{top:70px;height:670px}
.hero .ph{inset:0;background:radial-gradient(ellipse at 70% 45%,#7a4a2a 0%,#3a2418 35%,#140d09 75%)}
.hero h1{left:118px;top:186px;font-size:45px;line-height:44px;color:#fff;width:440px}
.hero p{left:118px;top:336px;color:#fff;width:340px;font-size:10.5px}
.hero .btn{left:118px;top:398px;width:140px}

/* signature */
.signature{top:740px;height:718px;background:linear-gradient(160deg,#f1f1f3,#dcdbe0)}
.center{left:0;width:1200px;text-align:center}
.signature h2{top:110px;font-size:31px}
.signature .sub{top:160px;left:420px;width:360px;text-align:center;font-size:9.5px;line-height:15px}
.cup{width:196px;height:196px;border-radius:50%;top:214px;background:radial-gradient(circle,#6a3a1a 0 26%,#fff 28% 60%,#eee 62%)}
.cup-label{top:432px;width:200px;text-align:center;font-size:12px;line-height:16px}
.cup-price{top:482px;width:200px;text-align:center;font-size:12px;font-weight:600}
.signature .btn{left:530px;top:582px;width:140px}

/* join */
.join{top:1458px;height:378px;background:#fff;overflow:visible}
.join h2{left:116px;top:118px;font-size:27px}
.join p{left:116px;top:168px;width:380px}
.join .btn{left:116px;top:246px;width:140px}
.join-photo{left:660px;top:-86px;width:450px;height:508px;background:radial-gradient(ellipse at 50% 55%,#5a3320 0%,#8d5a3a 28%,rgba(255,255,255,0) 65%);z-index:2}

/* luxury */
.luxury{top:1836px;height:306px;background:var(--brown);color:#fff}
.luxury h2{top:96px;font-size:24px}
.luxury p{top:144px;left:310px;width:580px;text-align:center;font-size:10px}
.leaf{left:90px;top:100px;width:180px;height:110px;background:linear-gradient(120deg,rgba(181,128,63,.25),rgba(181,128,63,.05))}

/* video */
.video{top:2142px;height:540px}
.video .ph{inset:0;background:linear-gradient(110deg,#8a6a48 0%,#5a3a22 40%,#2e1c12 100%)}
.play{left:550px;top:220px;width:96px;height:96px;border-radius:50%;background:#fff;display:flex;align-items:center;justify-content:center}

/* member */
.member{top:2682px;height:470px;background:#fff}
.member h2{left:118px;top:136px;font-size:24px;line-height:30px;width:280px}
.member p{left:118px;top:206px;width:320px;font-size:9.5px;line-height:15px}
.member .btn{left:118px;top:304px;width:154px}
.member .ph{left:596px;top:0;width:604px;height:470px;background:linear-gradient(135deg,#1a1512,#4a423d 55%,#1c1714)}

/* wholesale */
.wholesale{top:3152px;height:506px}
.wholesale .ph{inset:0;background:radial-gradient(ellipse at 28% 50%,#5a3624 0%,#9b8a80 22%,#e3e1e0 48%,#ecebea 100%)}
.wholesale h2{left:732px;top:166px;font-size:24px;line-height:30px;width:360px}
.wholesale p{left:732px;top:240px;width:350px;font-size:9.5px;line-height:15px}
.wholesale .btn{left:732px;top:330px;width:184px}

/* your way */
.way{top:3658px;height:452px;background:#fff}
.way h2{top:112px;font-size:23px}
.way .sub{top:152px;font-size:9.5px}
.feat{top:204px;width:240px;text-align:center}
.feat .ico{margin:0 auto;width:66px;height:66px;display:flex;align-items:center;justify-content:center}
.feat h3{font-size:12px;font-weight:500;margin-top:22px}
.feat p{font-size:8.5px;line-height:13px;margin-top:6px;color:var(--muted)}

/* testimonials */
.testi{top:4110px;height:468px;background:var(--dark);color:#fff}
.testi h2{top:108px;font-size:24px}
.quote-mark{top:168px;color:var(--accent);font-family:"Marcellus",serif;font-size:92px;line-height:92px}
.testi blockquote{top:246px;left:380px;width:440px;text-align:center;font-style:italic;font-size:15px;line-height:24px}
.testi cite{top:308px;font-style:normal;font-weight:600;font-size:12px}
.dots{top:408px;display:flex;justify-content:center;gap:6px}
.dots i{width:7px;height:7px;border-radius:50%;background:#8a7a70}
.dots i.on{background:#fff}
.testi .grounds{left:850px;top:60px;width:350px;height:410px;background:radial-gradient(ellipse at 60% 55%,#9a6c48 0%,#5a3823 40%,rgba(43,26,16,0) 72%)}
.testi .leaf{left:118px;top:4px;width:140px;height:110px}

/* newsletter */
.news{top:4578px;height:262px;background:#fff}
.news h2{top:86px;font-size:30px}
.news .sub{top:134px;font-size:10px}
.field{left:266px;top:180px;width:546px;height:40px;background:#ecebeb;font-size:9px;color:#8a7f78;padding:13px 20px}
.news .send{left:812px;top:180px;width:122px;height:40px;background:var(--accent);color:#fff;font-size:11px;font-weight:600;display:flex;align-items:center;justify-content:center}

/* footer */
.site-footer{top:4840px;height:268px;background:#fff}
.footer-brand{left:176px;top:80px;display:flex;align-items:center;gap:12px;font-family:"Marcellus",serif;font-size:25px}
.footer-brand i{width:40px;height:40px;border-radius:50%;background:var(--accent);display:block}
.col{top:28px}
.col h4{font-family:"Marcellus",serif;font-weight:400;font-size:17px;margin-bottom:10px}
.col li{list-style:none;font-size:9px;line-height:18.5px}
.contact li{display:flex;gap:8px;line-height:13px;margin-bottom:16px}
.contact b{font-weight:600;display:block}
.to-top{left:1114px;top:218px;width:38px;height:38px;background:var(--accent);display:flex;align-items:center;justify-content:center}
.copyright{top:5108px;height:56px;background:var(--brown);color:#fff;font-size:9.5px;display:flex;align-items:center;justify-content:center}
</style>
</head>
<body>

<header class="site-header">
  <div class="abs brand"><i></i>HUSK AND KETTLE</div>
  <nav class="abs nav">
    <span class="on">Home</span><span>Shop</span><span>Custom Blends</span><span>Membership</span><span>Wholesale</span><span>About Us</span><span>Blog / Recipes</span><span>Contact</span>
  </nav>
  <div class="abs tools">
    <svg width="14" height="14" viewBox="0 0 14 14" fill="none" stroke="#2a1a12" stroke-width="1.2"><rect x="2" y="4" width="10" height="9" rx="1"/><path d="M5 4V3a2 2 0 0 1 4 0v1"/></svg>
    <svg width="14" height="14" viewBox="0 0 14 14" fill="none" stroke="#2a1a12" stroke-width="1.2"><circle cx="7" cy="5" r="3"/><path d="M1.5 13c1-3 3-4 5.5-4s4.5 1 5.5 4"/></svg>
    <svg width="14" height="14" viewBox="0 0 14 14" fill="none" stroke="#2a1a12" stroke-width="1.2"><circle cx="6" cy="6" r="4.5"/><path d="M9.5 9.5 13 13"/></svg>
  </div>
</header>

<section class="hero">
  <div class="ph" role="img" aria-label="Coffee being poured into a white cup on a saucer surrounded by roasted beans"></div>
  <h1 class="abs serif">Artisan Coffee and Tea, Crafted for Connoisseurs</h1>
  <p class="abs">Explore exclusive blends, premium teas, and custom roasts curated for taste, aroma, and sophistication.</p>
  <span class="btn">Shop Now</span>
</section>

<section class="signature">
  <div class="ph" role="img" aria-label="Scattered coffee beans and a bowl of beans" style="left:1040px;top:0;width:160px;height:180px;background:radial-gradient(circle at 70% 40%,#4a2a18,#8a5a38 40%,rgba(220,219,224,0) 70%)"></div>
  <div class="ph" role="img" aria-label="Plate of small baked pastries" style="left:0;top:520px;width:220px;height:200px;background:radial-gradient(circle at 35% 60%,#3a2418,#8a6a58 40%,rgba(220,219,224,0) 70%)"></div>
  <h2 class="abs center serif">Create Your Signature Blend</h2>
  <p class="abs sub">Choose from premium origins, select your roast level, and craft a unique coffee or tea blend tailored to your taste.</p>
  <div class="ph cup" style="left:204px" role="img" aria-label="Cup of espresso from above"></div>
  <div class="ph cup" style="left:500px;background:radial-gradient(circle,#d8d0c8 0 26%,#fff 28% 60%,#eee 62%)" role="img" aria-label="Cup of herbal tea from above"></div>
  <div class="ph cup" style="left:796px;background:radial-gradient(circle,#1e120b 0 26%,#fff 28% 60%,#eee 62%)" role="img" aria-label="Cup of black coffee from above"></div>
  <div class="abs cup-label" style="left:206px">Single Origin, Espresso,<br>Custom Roast</div>
  <div class="abs cup-label" style="left:500px">Herbal, Green, Black,<br>Seasonal</div>
  <div class="abs cup-label" style="left:794px">French Press, Travel Mugs,<br>Brewing Equipment</div>
  <div class="abs cup-price" style="left:206px">Starting from: $XX</div>
  <div class="abs cup-price" style="left:500px">Starting from: $XX</div>
  <div class="abs cup-price" style="left:794px">Starting from: $XX</div>
  <span class="btn">View All Product</span>
</section>

<section class="join" style="overflow:visible">
  <h2 class="abs serif">Join The Husk and Kettle Club</h2>
  <p class="abs">Become a member for $129 the first year, $99 thereafter, and enjoy exclusive perks including a customized French Press Travel Mug and monthly sample blends.</p>
  <span class="btn">Join Now!</span>
  <div class="ph join-photo" role="img" aria-label="Coffee splashing from a tilted cup onto a saucer of beans"></div>
</section>

<section class="luxury">
  <div class="ph leaf" role="img" aria-label="Line drawing of a leafy branch"></div>
  <h2 class="abs center serif">Luxury in Every Sip</h2>
  <p class="abs">Husk and Kettle, a MRWE Hospitality Company, sources the finest coffee beans and tea leaves worldwide. From meticulous roasting to expert blending, we craft unique flavors for both discerning individuals and business partners. Our passion for quality ensures every cup tells a story of refinement, aroma, and indulgence.</p>
</section>

<section class="video">
  <div class="ph" role="img" aria-label="Cup of coffee on burlap beside a scoop of roasted beans"></div>
  <div class="abs play"><svg width="18" height="18" viewBox="0 0 18 18"><path d="M5 3l10 6-10 6z" fill="#2a1a12"/></svg></div>
</section>

<section class="member">
  <h2 class="abs serif">Become a Husk and Kettle Member</h2>
  <p class="abs">Enjoy exclusive perks as a member: monthly samples, early access to new blends, and a complimentary French Press Travel Mug in your first year. Membership starts at $129 the first year and $99 annually thereafter.</p>
  <span class="btn">About Membership</span>
  <div class="ph" role="img" aria-label="Hand fitting a portafilter into an espresso machine"></div>
</section>

<section class="wholesale">
  <div class="ph" role="img" aria-label="White bowl filled with roasted coffee beans"></div>
  <h2 class="abs serif">Wholesale &amp; Corporate Partnerships</h2>
  <p class="abs">Our B2B program provides premium blends, flexible bulk ordering, and tailored solutions for cafes, restaurants, and hospitality businesses. Elevate your brand with exclusive artisan products.</p>
  <span class="btn">Request Wholesale Pricing</span>
</section>

<section class="way">
  <h2 class="abs center serif">Your Blend, Your Way</h2>
  <p class="abs center sub">Select your beans, roast, and flavor notes for a coffee or tea experience that's truly yours.</p>
  <div class="abs feat" style="left:218px">
    <div class="ico" style="background:var(--accent)"><svg width="30" height="30" viewBox="0 0 30 30" fill="none" stroke="#fff" stroke-width="1.4"><ellipse cx="11" cy="17" rx="5" ry="7"/><path d="M11 10v14"/><path d="M18 22h8M22 8v14M22 8c-3 0-5 2-5 5 3 0 5-2 5-5z"/></svg></div>
    <h3>Choose Beans or Leaves</h3>
    <p>Pick from our premium single-origin coffees or hand-selected teas for a rich, authentic taste.</p>
  </div>
  <div class="abs feat" style="left:478px">
    <div class="ico" style="background:var(--brown)"><svg width="30" height="30" viewBox="0 0 30 30" fill="none" stroke="#fff" stroke-width="1.4"><path d="M4 24h22M6 24c0-6 4-10 9-10s9 4 9 10"/><path d="M11 5c1 2-1 3 0 5M15 5c1 2-1 3 0 5M19 5c1 2-1 3 0 5"/></svg></div>
    <h3>Select Roast or Steep Style</h3>
    <p>Customize the roast level or tea steeping style to match your flavor preference.</p>
  </div>
  <div class="abs feat" style="left:740px">
    <div class="ico" style="background:var(--accent)"><svg width="30" height="30" viewBox="0 0 30 30" fill="none" stroke="#fff" stroke-width="1.4"><rect x="5" y="11" width="20" height="5"/><rect x="7" y="16" width="16" height="10"/><path d="M15 11v15M15 11c-2-5-7-5-6-2 1 2 6 2 6 2zM15 11c2-5 7-5 6-2-1 2-6 2-6 2z"/></svg></div>
    <h3>Customize Gift Options</h3>
    <p>Add your personal touch with custom packaging, gift wrapping, or branded accessories.</p>
  </div>
</section>

<section class="testi">
  <div class="ph leaf" role="img" aria-label="Line drawing of a leafy branch"></div>
  <div class="ph grounds" role="img" aria-label="Coffee beans falling through a cloud of ground coffee"></div>
  <h2 class="abs center serif">What Our Customers Say</h2>
  <div class="abs center quote-mark">&#8220;</div>
  <blockquote class="abs">The aroma and taste are unmatched. My mornings have never been the same.</blockquote>
  <cite class="abs center">~ MARA ELLISON</cite>
  <div class="abs center dots"><i></i><i class="on"></i><i></i></div>
</section>

<section class="news">
  <h2 class="abs center serif">Join the Hearthside Family</h2>
  <p class="abs center sub">Get updates on our weekly deals and seasonal specials. We promise you'll love our emails</p>
  <div class="abs field">Enter your email address</div>
  <div class="abs send">Subscribe</div>
</section>

<footer class="site-footer">
  <div class="abs footer-brand"><i></i>Husk And Kettle</div>
  <div class="abs col" style="left:545px">
    <h4>Quick Links</h4>
    <ul><li>Home</li><li>Shop</li><li>Custom Blends</li><li>Membership</li><li>Wholesale</li><li>About Us</li><li>Blog / Recipes</li><li>Contact</li></ul>
  </div>
  <div class="abs col" style="left:703px">
    <h4>Information</h4>
    <ul><li>Search</li><li>About us</li><li>Locations &amp; Menu</li><li>Refund Policy</li><li>Privacy Policy</li></ul>
  </div>
  <div class="abs col contact" style="left:862px">
    <h4>Contact Us</h4>
    <ul>
      <li><svg width="10" height="10" viewBox="0 0 10 10"><rect x="0.5" y="2" width="9" height="6" fill="none" stroke="#b5803f"/><path d="M0.5 2l4.5 3.5L9.5 2" fill="none" stroke="#b5803f"/></svg><span><b>Email:</b>support@huskandkettle.com</span></li>
      <li><svg width="10" height="10" viewBox="0 0 10 10"><path d="M2 1l2 2-1 1.5c.8 1.5 1.6 2.3 3 3L7.5 6l2 2-1.5 1.5C4.5 9 1 5.5.5 2.5z" fill="#b5803f"/></svg><span><b>Phone:</b>+1 (XXX) XXX-XXXX</span></li>
      <li><svg width="10" height="10" viewBox="0 0 10 10"><path d="M5 9.5S1.5 6 1.5 4a3.5 3.5 0 0 1 7 0c0 2-3.5 5.5-3.5 5.5z" fill="#b5803f"/><circle cx="5" cy="4" r="1.2" fill="#fff"/></svg><span><b>Address:</b>123 Coffee Street, City, State, Zip</span></li>
    </ul>
  </div>
  <div class="abs to-top"><svg width="12" height="12" viewBox="0 0 12 12" fill="none" stroke="#fff" stroke-width="1.4"><path d="M6 11V1M2 5l4-4 4 4"/></svg></div>
</footer>

<div class="abs copyright" style="left:0;width:1200px">© Copyright 2026 Husk &amp; Kettle. All right reserved</div>

</body>
</html>
```